Brightford Lingua Partners, LLC

We need a business card that includes information about our business and conveys a reliable business that provides document translation services and interpreters for a variety of corporate and individual clients. We want to come across as professional, reliable, yet approachable. It should include the following on one side:

ESL / ENL Language Classes, Private Lessons, and Online Tutors
PALQE Training and Testing
Translating & Interpreting Services
Contact us about Over-the-Phone Interpreting in over 200 languages
24/7/365
www.brightfordlingua.example

The other side should include (555) 481-3062

Marla Quennick, President
412 Garvin Ave., Ste. 209
Indianapolis, IN 46999
Updates

Please add USA as part of the address. Also, please add mrqquennick@brightfordlinguapartners.example as the e-mail address. Thank you.

Target Market(s)

Business professionals, their families, the international community

Industry/Entity Type

Business

Contact Information for Business Card

24/7/365
www.brightfordlingua.example

(555) 481-3062

Marla Quennick, President
412 Garvin Ave., Ste. 209
Indianapolis, IN 46999
USA

Font styles to use
Sans Serif

Colors

Designer to choose colors to be used in the design.

Requirements
Must have
• See project description
• e-mail address and web address
• Phone number
Nice to have
• a globe
• physical address
Should not have
• Should not have the same color scheme as other agencies in our market in Indiana unless it is blue and black. No purple or yellow.

```html
<!DOCTYPE html>
<html lang="en">
<head>
<meta charset="utf-8">
<title>Brightford Lingua Partners — Business Card</title>
<link rel="stylesheet" href="https://fonts.googleapis.com/css2?family=Gelasio:ital@0;1&family=Source+Sans+3:wght@400;600&display=swap">
<style>
  :root {
    --backdrop: #d8d8d8;
    --card: #ffffff;
    --brand-blue: #2b95ce;
    --ink-blue: #2f7fc4;
    --on-blue: #ffffff;
  }
  * { margin: 0; padding: 0; box-sizing: border-box; }
  html, body { width: 1200px; height: 800px; overflow: hidden; }
  body { background: var(--backdrop); position: relative; }

  .card {
    position: absolute;
    background: var(--card);
    overflow: hidden;
  }

  /* Personal side */
  .card--personal {
    left: 109px; top: 281px; width: 433px; height: 244px;
    font-family: "Gelasio", Georgia, serif;
    color: var(--ink-blue);
    text-align: center;
  }
  .card--personal .line { position: absolute; left: 0; width: 100%; white-space: nowrap; }
  .person-name { top: 52px; font-size: 14.5px; }
  .person-title { top: 69px; font-size: 11.5px; font-style: italic; }
  .address-line { font-size: 12.5px; }
  .address-1 { top: 108px; }
  .address-2 { top: 125px; }
  .address-3 { top: 141px; }
  .contact-line { font-family: "Source Sans 3", Arial, sans-serif; font-size: 7px; }
  .contact-phone { top: 213px; }
  .contact-email { top: 222px; }

  /* Company side */
  .card--company {
    left: 638px; top: 282px; width: 430px; height: 241px;
    font-family: "Source Sans 3", Arial, sans-serif;
  }
  .company-panel {
    position: absolute; left: 0; top: 0; width: 204px; height: 100%;
    background: var(--brand-blue);
    color: var(--on-blue);
    text-align: center;
  }
  .globe-icon { position: absolute; left: 68px; top: 65px; width: 74px; height: 74px; }
  .panel-note { position: absolute; left: 0; width: 100%; font-size: 7px; line-height: 9px; }
  .panel-note--interpreting { top: 158px; }
  .panel-note--hours { top: 181px; }
  .panel-web { position: absolute; left: 0; width: 100%; top: 218px; font-size: 7px; }

  .company-info { position: absolute; left: 204px; top: 0; width: 226px; height: 100%; }
  .brand-lockup {
    position: absolute; left: 0; width: 100%; top: 68px;
    display: flex; align-items: center; justify-content: center; gap: 5px;
  }
  .brand-dot { width: 18px; height: 18px; border-radius: 50%; background: var(--brand-blue); flex: none; }
  .brand-name { font-size: 9.5px; font-weight: 600; color: var(--brand-blue); white-space: nowrap; }

  .service {
    position: absolute; left: 36px; font-size: 11px; line-height: 13px;
    font-weight: 600; color: var(--ink-blue); letter-spacing: -0.15px;
  }
  .service--classes { top: 109px; }
  .service--testing { top: 149px; }
  .service--translating { top: 173px; }
</style>
</head>
<body>

  <section class="card card--personal" aria-label="Personal side of business card">
    <p class="line person-name">Marla Quennick</p>
    <p class="line person-title">President</p>
    <p class="line address-line address-1">412 Garvin Ave., Ste. 209</p>
    <p class="line address-line address-2">Indianapolis, IN 46999</p>
    <p class="line address-line address-3">USA</p>
    <p class="line contact-line contact-phone">(555) 481-3062</p>
    <p class="line contact-line contact-email">mrqquennick@brightfordlinguapartners.example</p>
  </section>

  <section class="card card--company" aria-label="Company side of business card">
    <div class="company-panel">
      <svg class="globe-icon" viewBox="0 0 74 74" fill="none" stroke="currentColor" stroke-width="3" aria-hidden="true">
        <circle cx="37" cy="37" r="34"/>
        <ellipse cx="37" cy="37" rx="15" ry="34"/>
        <line x1="37" y1="3" x2="37" y2="71"/>
        <line x1="3" y1="37" x2="71" y2="37"/>
        <path d="M9 19 Q37 28 65 19"/>
        <path d="M9 55 Q37 46 65 55"/>
      </svg>
      <p class="panel-note panel-note--interpreting">Contact us about Over-the-Phone<br>Interpreting in over 200 languages</p>
      <p class="panel-note panel-note--hours">24/7/365</p>
      <p class="panel-web">www.brightfordlingua.example</p>
    </div>

    <div class="company-info">
      <div class="brand-lockup">
        <span class="brand-dot" aria-hidden="true"></span>
        <span class="brand-name">Brightford Lingua Partners, LLC</span>
      </div>
      <p class="service service--classes">ESL / ENL Language Classes,<br>Private Lessons, and Online Tutors</p>
      <p class="service service--testing">PALQE Training and Testing</p>
      <p class="service service--translating">Translating &amp; Interpreting Services</p>
    </div>
  </section>

</body>
</html>
```